Calloway Grove Golden Swift Nest needs a sticker design

We need a sticker design to be pasted on the top of our current acrylic box packaging. The sticker design can be derived from our website design at calloway-grove.sg. The sticker design should show some characteristic of 60% Indonesia (where the edible bird nest is harvested) and 40% Singapore (where the edible bird nest is sold). The sticker design should incorporate chinese word for edible bird nest: 燕窩. Thank you for your kind consideration
Target Market(s)
Singaporean chinese customers
Industry/Entity Type
Food Production
Font styles to use
Requirements
Must have
- - Calloway Grove Swift Nest logo attached (please help to delete the chinese wording inside the logo and english wording below the logo)
- - Product name: Calloway Grove Golden Swift Nest
- - Some characteristic of 60% Indonesia (where the edible bird nest is harvested) and 40% Singapore (where the edible bird nest is sold). Maybe to incorporate some batik design or national flags
- - The chinese word for edible bird nest: 燕窩 (can be in the background)
- - The phrase: 100% Natural
- - The phrase: Harvested from pristine locations in Indonesia
- - Big transparent window to be able to see the product inside the box
- (pls see our competitor packaging 2 - attached)
- - Size of the sticker: width from left to right 15cm, height 12cm
Should not have
- - black color

```html
<!DOCTYPE html>
<html lang="en">
<head>
<meta charset="utf-8">
<title>Calloway Grove Golden Swift Nest – Sticker</title>
<link rel="stylesheet" href="https://fonts.googleapis.com/css2?family=Rozha+One&family=Tinos&family=Noto+Serif+SC:wght@500&display=swap">
<style>
  :root {
    --sticker-red: #d8202a;
    --sticker-red-deep: #c01822;
    --gold: #f6c84a;
    --gold-light: #fbe08f;
    --gold-deep: #d99a1e;
    --cream: #fff6d6;
    --window-white: #ffffff;
    --nest-light: #e9dcc0;
    --nest-mid: #cbb992;
    --canvas-bg: #ffffff;
  }
  * { box-sizing: border-box; margin: 0; padding: 0; }
  html, body {
    width: 694px; height: 1200px; overflow: hidden;
    background: var(--canvas-bg);
  }
  .canvas { position: relative; width: 694px; height: 1200px; }
  .sticker {
    position: absolute; left: 5px; width: 683px; height: 573px;
    background: radial-gradient(circle at 50% 40%, var(--sticker-red) 0%, var(--sticker-red-deep) 100%);
  }
  .sticker--empty { top: 5px; }
  .sticker--filled { top: 591px; }
  .sticker__title {
    position: absolute; left: 0; right: 0; top: 36px;
    text-align: center;
    font-family: "Rozha One", Georgia, serif;
    font-size: 35px; line-height: 1; letter-spacing: 0.3px;
    color: var(--gold);
  }
  .window-frame { position: absolute; left: 24px; top: 104px; width: 442px; height: 458px; }
  .side-panel {
    position: absolute; left: 488px; width: 194px; top: 100px;
    text-align: center; color: var(--gold-light);
    font-family: "Tinos", "Times New Roman", serif;
  }
  .side-panel__hanzi {
    font-family: "Noto Serif SC", serif;
    font-size: 32px; line-height: 1; color: var(--gold);
  }
  .brand-mark { margin-top: 22px; display: flex; flex-direction: column; align-items: center; gap: 10px; }
  .brand-mark__dot { width: 40px; height: 40px; border-radius: 50%; border: 3px solid var(--gold); }
  .brand-mark__name { font-size: 20px; line-height: 1.15; color: var(--gold); }
  .side-panel__claim { margin-top: 24px; font-size: 25px; line-height: 1; color: var(--gold); }
  .side-panel__story { margin-top: 18px; font-size: 16px; line-height: 1.45; }
  .side-panel__origin { margin-top: 26px; font-size: 16px; line-height: 1.45; }
</style>
</head>
<body>
<main class="canvas">

  <section class="sticker sticker--empty">
    <h1 class="sticker__title">Calloway Grove Golden Swift Nest</h1>
    <svg class="window-frame" viewBox="0 0 442 458" aria-hidden="false">
      <rect x="3" y="3" width="436" height="452" fill="none" stroke="var(--gold)" stroke-width="6"/>
      <rect x="14" y="14" width="414" height="430" fill="none" stroke="var(--gold)" stroke-width="2"/>
      <g role="img" aria-label="Gold corner ornaments and floral pattern">
        <circle cx="44" cy="44" r="24" fill="var(--gold-deep)" opacity="0.55"/>
        <circle cx="398" cy="44" r="24" fill="var(--gold-deep)" opacity="0.55"/>
        <circle cx="44" cy="414" r="24" fill="var(--gold-deep)" opacity="0.55"/>
        <circle cx="398" cy="414" r="24" fill="var(--gold-deep)" opacity="0.55"/>
      </g>
      <circle role="img" aria-label="Gold key-pattern ring around the window" cx="220" cy="222" r="193" fill="var(--gold)"/>
      <circle cx="220" cy="222" r="168" fill="var(--sticker-red)"/>
      <circle cx="220" cy="222" r="160" fill="var(--gold)"/>
      <circle cx="220" cy="222" r="156" fill="var(--window-white)"/>
    </svg>
    <aside class="side-panel">
      <p class="side-panel__hanzi">燕窩</p>
      <div class="brand-mark">
        <span class="brand-mark__dot"></span>
        <span class="brand-mark__name">Calloway Grove<br>Swift Nest</span>
      </div>
      <p class="side-panel__claim">100% Natural</p>
      <p class="side-panel__story">Some characteristic of 60% Indonesia (where the edible bird nest is harvested) and 40% Singapore (where the edible bird nest is sold)</p>
      <p class="side-panel__origin">Harvested from pristine locations in Indonesia</p>
    </aside>
  </section>

  <section class="sticker sticker--filled">
    <h1 class="sticker__title">Calloway Grove Golden Swift Nest</h1>
    <svg class="window-frame" viewBox="0 0 442 458">
      <defs>
        <radialGradient id="nest-tone" cx="50%" cy="45%" r="60%">
          <stop offset="0%" stop-color="var(--nest-light)"/>
          <stop offset="100%" stop-color="var(--nest-mid)"/>
        </radialGradient>
      </defs>
      <rect x="3" y="3" width="436" height="452" fill="none" stroke="var(--gold)" stroke-width="6"/>
      <rect x="14" y="14" width="414" height="430" fill="none" stroke="var(--gold)" stroke-width="2"/>
      <g role="img" aria-label="Gold corner ornaments and floral pattern">
        <circle cx="44" cy="44" r="24" fill="var(--gold-deep)" opacity="0.55"/>
        <circle cx="398" cy="44" r="24" fill="var(--gold-deep)" opacity="0.55"/>
        <circle cx="44" cy="414" r="24" fill="var(--gold-deep)" opacity="0.55"/>
        <circle cx="398" cy="414" r="24" fill="var(--gold-deep)" opacity="0.55"/>
      </g>
      <circle role="img" aria-label="Gold key-pattern ring around the window" cx="220" cy="222" r="193" fill="var(--gold)"/>
      <circle cx="220" cy="222" r="168" fill="var(--sticker-red)"/>
      <circle cx="220" cy="222" r="160" fill="var(--gold)"/>
      <circle role="img" aria-label="Edible bird nest cups seen through the window" cx="220" cy="222" r="156" fill="url(#nest-tone)"/>
    </svg>
    <aside class="side-panel">
      <p class="side-panel__hanzi">燕窩</p>
      <div class="brand-mark">
        <span class="brand-mark__dot"></span>
        <span class="brand-mark__name">Calloway Grove<br>Swift Nest</span>
      </div>
      <p class="side-panel__claim">100% Natural</p>
      <p class="side-panel__story">Some characteristic of 60% Indonesia (where the edible bird nest is harvested) and 40% Singapore (where the edible bird nest is sold)</p>
      <p class="side-panel__origin">Harvested from pristine locations in Indonesia</p>
    </aside>
  </section>

</main>
</body>
</html>
```